Brisk Bites natural dog treats

We need a packaging design for a new brand of natural dog treats named Brisk Bites. Need the color scheme and template for the line of products that will be on flexible pouches or stand upright gusseted pouches.

Target Market(s)

Mass appeal with the majority being female. This will be a grocery store brand moderate price.

Industry/Entity Type

Grocery Store

Font styles to use
Serif
Sans Serif

Requirements
Must have
• Clean bright colors preferably yellow light blue etc. Very clean, memorable and simple packaging. This being a natural product it should also show natural with the packaging.
Nice to have
• Dog 30-50% of the packaging to be clear to show the product.
Should not have
• Not busy
Too much information on the front.

```html
<!DOCTYPE html>
<html lang="en">
<head>
<meta charset="utf-8">
<title>Brisk Bites Beef Sticks Pouch</title>
<link rel="stylesheet" href="https://fonts.googleapis.com/css2?family=Oswald:wght@500;600;700&family=Russo+One&family=Fredoka:wght@600&family=Titan+One&display=swap">
<style>
  :root {
    --stage: #e9e9ea;
    --pouch-orange: #ef922f;
    --pouch-edge: #d8701c;
    --pouch-glow: #f6b56a;
    --purple: #6a3c8c;
    --purple-band: #4e2464;
    --ink-dark: #2a1838;
    --white: #ffffff;
    --product-dark: #8e4a2c;
    --product-light: #c9855a;
  }
  html, body {
    margin: 0;
    width: 1200px;
    height: 1200px;
    overflow: hidden;
    background: var(--stage);
  }
  .canvas {
    position: relative;
    width: 1200px;
    height: 1200px;
  }
  .pouch {
    position: absolute;
    left: 305px;
    top: 95px;
    width: 615px;
    height: 990px;
    background: linear-gradient(90deg, var(--pouch-edge) 0 22px, var(--pouch-orange) 22px calc(100% - 22px), var(--pouch-edge) calc(100% - 22px));
    overflow: hidden;
  }
  .pouch-seal {
    position: absolute;
    left: 0; right: 0; top: 0;
    height: 42px;
    background: var(--pouch-edge);
  }
  .tagline {
    position: absolute;
    top: 100px; left: 0; right: 0;
    text-align: center;
    font-family: "Russo One", sans-serif;
    font-size: 21px;
    line-height: 24px;
    color: var(--purple);
    letter-spacing: 0.5px;
  }
  .brand {
    position: absolute;
    top: 166px; left: 0; right: 0;
    display: flex;
    justify-content: center;
    align-items: center;
    gap: 14px;
  }
  .brand-dot {
    width: 44px; height: 44px;
    border-radius: 50%;
    background: var(--white);
  }
  .brand-name {
    font-family: "Fredoka", sans-serif;
    font-weight: 600;
    font-size: 34px;
    line-height: 44px;
    color: var(--white);
  }
  .product-title {
    position: absolute;
    top: 222px; left: 0; right: 0;
    text-align: center;
    font-family: "Titan One", sans-serif;
    color: var(--purple);
    -webkit-text-stroke: 18px var(--white);
    paint-order: stroke fill;
    line-height: 0.98;
    margin: 0;
    font-weight: 400;
  }
  .product-title span { display: block; }
  .product-title .line-one { font-size: 118px; }
  .product-title .line-two { font-size: 108px; }
  .window {
    position: absolute;
    left: 0; top: 455px;
    width: 615px; height: 285px;
  }
  .claim {
    position: absolute;
    top: 742px; left: 0; right: 0;
    text-align: center;
    font-family: "Oswald", sans-serif;
    font-weight: 600;
    font-size: 32px;
    line-height: 34px;
    color: var(--purple-band);
  }
  .benefit-band {
    position: absolute;
    top: 778px; left: 22px; right: 22px;
    height: 112px;
    background: var(--purple-band);
    color: var(--white);
    text-align: center;
  }
  .benefit-band .subline {
    font-family: "Oswald", sans-serif;
    font-weight: 600;
    font-size: 23px;
    line-height: 28px;
    margin-top: 10px;
  }
  .badges {
    display: flex;
    justify-content: center;
    gap: 22px;
    margin-top: 10px;
  }
  .badge {
    width: 50px; height: 50px;
    border: 2px solid var(--white);
    border-radius: 50%;
    display: flex;
    align-items: center;
    justify-content: center;
    font-family: "Oswald", sans-serif;
    font-weight: 500;
    font-size: 11px;
    line-height: 1.15;
  }
  .net-label {
    position: absolute;
    top: 900px; left: 0; right: 0;
    text-align: center;
    font-family: "Oswald", sans-serif;
    font-weight: 600;
    font-size: 19px;
    line-height: 24px;
    color: var(--ink-dark);
  }
  .net-weight {
    position: absolute;
    top: 926px; left: 0; right: 0;
    text-align: center;
    font-family: "Oswald", sans-serif;
    font-weight: 700;
    font-size: 40px;
    line-height: 48px;
    color: var(--ink-dark);
  }
</style>
</head>
<body>
<div class="canvas">
  <div class="pouch">
    <div class="pouch-seal"></div>
    <div class="tagline">COMPLEMENTARY PET FOOD FOR DOGS</div>
    <div class="brand">
      <span class="brand-dot"></span>
      <span class="brand-name">Brisk Bites</span>
    </div>
    <h1 class="product-title">
      <span class="line-one">BEEF</span>
      <span class="line-two">STICKS</span>
    </h1>

    <svg class="window" viewBox="0 0 615 300" preserveAspectRatio="none" xmlns="http://www.w3.org/2000/svg">
      <defs>
        <linearGradient id="product-fill" x1="0" y1="0" x2="1" y2="0">
          <stop offset="0" stop-color="#8e4a2c"/>
          <stop offset="0.5" stop-color="#c9855a"/>
          <stop offset="1" stop-color="#8e4a2c"/>
        </linearGradient>
      </defs>
      <g class="window-halo" fill="#f6b56a" opacity="0.7">
        <rect x="100" y="40" width="415" height="220"/>
        <circle cx="130" cy="80" r="72"/>
        <circle cx="130" cy="220" r="72"/>
        <circle cx="485" cy="80" r="72"/>
        <circle cx="485" cy="220" r="72"/>
      </g>
      <g class="window-product" role="img" aria-label="Clear window showing beef stick dog treats" fill="url(#product-fill)">
        <rect x="110" y="62" width="395" height="176"/>
        <circle cx="130" cy="82" r="58"/>
        <circle cx="130" cy="218" r="58"/>
        <circle cx="485" cy="82" r="58"/>
        <circle cx="485" cy="218" r="58"/>
      </g>
    </svg>

    <div class="claim">NATURAL DOG TREATS</div>
    <div class="benefit-band">
      <div class="subline">HEALTY AND DELICIOUS</div>
      <div class="badges">
        <div class="badge">TASTY<br>BEEF</div>
        <div class="badge">FARM<br>FRESH</div>
        <div class="badge">GLUTEN<br>FREE</div>
      </div>
    </div>
    <div class="net-label">NET WEIGHT</div>
    <div class="net-weight">4 OZ OF GOODNESS</div>
  </div>
</div>
</body>
</html>
```